Health care center needs brochure design

We need a set of brochure designs for the 4 sections of our clinic, color coded based on the brand guidelines and with introduced icons to every section. The three sections include Biological Medicine (main medication tool is the IV tool), The Brindle Path program (main medication tool are the detox tools) , the Aesthetics section ( main medication tool is the syringe) and the lab (main tool is the microscope). You can find out more about our sections in the website www.velnortaclinic-example.com. The use of elements of the brand itself such as the lotus is also applicable.

Industry/Entity Type

Health Care

Requirements
Must have
• use of brand identity colors and features
• reflective medical icons
• color coding for each of the 4 sections based on the brand colors
Should not have
• pictures overused by other health care providers

```html
<!DOCTYPE html>
<html lang="en">
<head>
<meta charset="utf-8">
<title>Velnorta Integrated Care Center – Tests and Diagnostics Brochure</title>
<link href="https://fonts.googleapis.com/css2?family=Open+Sans:wght@400;600;700&family=Oswald:wght@500&family=Varela+Round&display=swap" rel="stylesheet">
<style>
  :root{
    --page-bg:#ffffff;
    --paper-grey:#ebeced;
    --brand-green:#6fd88a;
    --brand-green-text:#5ccf79;
    --ink:#1e1e1e;
    --muted:#4a4a4a;
    --photo-light:#d9e8f0;
    --photo-mid:#b9d3e2;
    --photo-dark:#9fc2d6;
  }
  *{box-sizing:border-box;margin:0;padding:0}
  html,body{width:1200px;height:1200px;overflow:hidden;background:var(--page-bg)}
  .spread{position:absolute;left:50px;top:210px;width:1100px;height:780px;display:flex;box-shadow:0 6px 24px rgba(0,0,0,.12)}
  .page{position:relative;width:550px;height:780px;overflow:hidden}
  .page--inside{background:var(--paper-grey)}
  .section-title{position:absolute;left:46px;top:50px;font-family:"Oswald",sans-serif;font-size:26px;letter-spacing:.3px;color:var(--ink);display:flex;align-items:center;gap:10px}
  .section-title::before{content:"";width:22px;height:10px;background:var(--ink)}
  .section-title .accent{color:var(--brand-green-text)}
  .intro{position:absolute;left:46px;top:100px;width:250px;font-family:"Open Sans",sans-serif;font-size:14px;line-height:1.4;color:var(--ink)}
  .test-list{position:absolute;left:46px;top:156px;list-style:none;font-family:"Open Sans",sans-serif;font-size:10.5px;line-height:1.45;color:var(--muted)}
  .test-list li{display:flex;align-items:center;gap:7px}
  .test-list li::before{content:"";width:6px;height:6px;border-radius:50%;background:var(--brand-green)}
  .microscope-photo{position:absolute;left:330px;top:80px;width:170px;height:230px;border-radius:8px;background:linear-gradient(160deg,#dfe1e3,#b9bcc0)}
  .green-band{position:absolute;left:0;top:400px;width:550px;height:380px;background:var(--brand-green)}
  .name-panel{position:absolute;left:0;top:360px;width:420px;height:110px;background:var(--paper-grey);border-radius:0 0 50px 0;display:flex;align-items:center;justify-content:center;gap:12px}
  .brand-dot{width:54px;height:54px;border-radius:50%;background:var(--brand-green)}
  .brand-name{font-family:"Varela Round",sans-serif;font-size:17px;line-height:1.2;color:var(--brand-green-text)}
  .address{position:absolute;left:0;top:530px;width:550px;text-align:center;font-family:"Open Sans",sans-serif;font-weight:700;font-size:16px;line-height:1.45;color:var(--ink)}
  .page--cover{background:var(--photo-light)}
  .cover-photo{position:absolute;inset:0;background:linear-gradient(135deg,var(--photo-mid) 0%,var(--photo-light) 45%,var(--photo-dark) 100%)}
  .cover-brand{position:absolute;left:50px;top:480px;display:flex;flex-direction:column;align-items:center;gap:14px}
  .cover-brand .brand-dot{width:90px;height:90px}
  .cover-brand .brand-name{font-size:22px;text-align:center}
</style>
</head>
<body>
  <main class="spread">
    <section class="page page--inside">
      <h1 class="section-title">TESTS AND <span class="accent">DIAGNOSTICS</span></h1>
      <p class="intro">The Center provides a number of diagnostics and tests which include:</p>
      <ul class="test-list">
        <li>DNA Analysis</li>
        <li>Food Intolerance Test</li>
        <li>Hormone Test</li>
        <li>Dark Field Microscopy</li>
        <li>Digestion</li>
        <li>Body Composition Analysis</li>
        <li>Allergy Diagnostics</li>
        <li>ANS Analysis</li>
        <li>Lipid Analysis</li>
      </ul>
      <div class="microscope-photo" role="img" aria-label="Photo of a laboratory microscope"></div>
      <div class="green-band"></div>
      <div class="name-panel">
        <span class="brand-dot"></span>
        <span class="brand-name">VELNORTA<br>INTEGRATED<br>CARE CENTER</span>
      </div>
      <address class="address">
        Velnorta Integrated Care Center<br>
        PO Box 40412<br>
        Lakeview, Cedar Quay, Marlow South<br>
        United Arab Emirates<br>
        04-555 0192<br>
        info@velnortaclinic-example.com
      </address>
    </section>
    <section class="page page--cover">
      <div class="cover-photo" role="img" aria-label="Photo of a patient's arm with an IV line, a gloved hand holding a syringe"></div>
      <div class="cover-brand">
        <span class="brand-dot"></span>
        <span class="brand-name">VELNORTA<br>INTEGRATED<br>CARE CENTER</span>
      </div>
    </section>
  </main>
</body>
</html>
```